Lira Dovecott Music Flyer for Social Media

The flyer needs to include the networks Lira Dovecott music is distributed on such as uBeats, oWaveCast, Brume, and Sonarly. This flyer will be posted on social media websites such as friendloop, Snapwell, and Chirpex. The flyer will also be listed on the music artist official website. The artist logo is attached for additional creative ideas.

Target Market(s)

Music lovers

Industry/Entity Type

Music Download

Requirements
Must have
• Must have the music networks listed on the photo and the artist name.
Nice to have
• It would be nice to have the website listed: www.liradovecott.org and artist logo.
Should not have
• Anything that is not listed in the project description.

```html
<!DOCTYPE html>
<html lang="en">
<head>
<meta charset="utf-8">
<title>Lira Dovecott – Music Flyer</title>
<link rel="stylesheet" href="https://fonts.googleapis.com/css2?family=Cormorant+Garamond:wght@400;500&family=Montserrat:wght@400;600;700&display=swap">
<style>
  :root {
    --plum-deep: #3a2640;
    --plum-hair: #2c1d28;
    --lavender-light: #d9cbdc;
    --lavender-mid: #a68fab;
    --white: #ffffff;
    --white-soft: rgba(255,255,255,0.88);
  }
  * { margin: 0; padding: 0; box-sizing: border-box; }
  html, body {
    width: 1200px; height: 1200px; overflow: hidden;
    background: var(--plum-deep);
  }
  .flyer {
    position: relative; width: 1200px; height: 1200px;
    background: var(--plum-deep);
    color: var(--white);
  }
  .artist-portrait {
    position: absolute; left: 0; top: 106px; width: 1002px; height: 986px;
    background:
      radial-gradient(ellipse 32% 30% at 30% 42%, rgba(120,80,70,0.85), rgba(120,80,70,0) 100%),
      radial-gradient(ellipse 70% 60% at 40% 35%, var(--plum-hair) 0%, rgba(44,29,40,0.9) 45%, rgba(44,29,40,0) 80%),
      linear-gradient(160deg, var(--lavender-mid) 0%, var(--lavender-light) 55%, #cbb9cf 100%);
  }
  .brand-block {
    position: absolute; left: 600px; top: 200px; width: 560px;
    text-align: center;
  }
  .brand-initials {
    font-family: "Cormorant Garamond", serif;
    font-weight: 400; font-size: 170px; line-height: 1;
    color: var(--white); margin-left: -90px;
  }
  .artist-name {
    position: absolute; left: 620px; top: 452px; width: 500px;
    font-family: "Cormorant Garamond", serif;
    font-weight: 400; font-size: 34px; letter-spacing: 0.42em;
    text-transform: uppercase; white-space: nowrap; color: var(--white);
  }
  .artist-site {
    position: absolute; left: 700px; top: 520px; width: 350px;
    text-align: center;
    font-family: "Montserrat", sans-serif;
    font-weight: 400; font-size: 17px; letter-spacing: 0.14em;
    color: var(--white-soft);
  }
  .platforms {
    position: absolute; left: 620px; top: 680px; width: 500px;
    display: grid; grid-template-columns: 1fr 1fr; row-gap: 72px;
    list-style: none;
  }
  .platform {
    display: flex; align-items: center; gap: 12px;
    font-family: "Montserrat", sans-serif;
    font-weight: 700; font-size: 36px; color: var(--white);
  }
  .platform:nth-child(even) { justify-content: flex-end; }
  .platform-dot {
    width: 34px; height: 34px; border-radius: 50%;
    background: var(--white); flex: none;
  }
</style>
</head>
<body>
  <main class="flyer">
    <div class="artist-portrait" role="img" aria-label="Portrait of the smiling artist with voluminous curly hair, wearing a striped top"></div>

    <div class="brand-block">
      <div class="brand-initials">LD</div>
    </div>
    <h1 class="artist-name">Lira Dovecott</h1>
    <p class="artist-site">www.liradovecott.org</p>

    <ul class="platforms">
      <li class="platform"><span class="platform-dot"></span>uBeats</li>
      <li class="platform">Brume</li>
      <li class="platform"><span class="platform-dot"></span>Sonarly</li>
      <li class="platform">oWaveCast</li>
    </ul>
  </main>
</body>
</html>
```